Buch-/E-Book-Cover für Referenzbuch der Industrie
Zielgruppe
Als Manufaktur einzigartiger Fachmedien präsentiert verlag-wendemark Schlüsseltechnologien und ihre Märkte. Faszination für Technik ist die Grundlage unserer Arbeit. Mehr als 30 Jahre verlegerische Erfahrung und das Verständnis für Technologiemärkte machen uns zu einem anerkannten Partner der Industrie.
Unsere Medienmarken knüpfen ein starkes und weit verzweigtes Netzwerk – Print und digital – , in dem sich Anbieter und Anwender von Technologien und Produkten in ihren Zielsetzungen wiederfinden.
Unsere Magazine, Events und Netzwerkveranstaltungen sowie kundenspezifische Kommunikations- & Strategiekampagnen setzen in ihren Zielmärkten Maßstäbe und genießen bei Lesern, Kunden und Partnern Vertrauen und Respekt.
Für das ausgeschriebene Projekt handelt es sich um unsere Referenzpublikation FACTORY.onward MOLUTAVA.
MOLUTAVA {polynesisch: Freiraum}
Das Referenzbuch der Industrie. Für Vorwärtsdenker und Zukunftsmacher.
Wandel bestimmt unsere Zeit und verändert unsere Gesellschaft, unsere Unternehmen, uns alle.
Im Wandel liegt Freiraum zur Gestaltung. Gesellschaftlicher Wandel, Technologie-Wandel, Klimawandel, Wertewandel, Führungswandel oder Organisationswandel sind nur einige Beispiele. Wer dabei den Wandel in engen Bahnen denkt, verschenkt Potential. Veränderung braucht Freiraum für neue Ideen und Perspektiven sowie Persönlichkeiten, die diesen nutzen wollen.
Aber wer gestaltet die Zukunft der Industrie und ihrer Branchen? Und wie?
Wir geben Personen aus der Industrie den Freiraum, ihre Perspektiven auf und aus dem Wandel zu erzählen. Warum? Weil sie uns begeistert haben, in persönlichen Treffen und Gesprächen, durch streitbare Meinungen und ehrliche Geschichten. Weil sie die Zukunft verändern.
MOLUTAVA ist eine Aufforderung: Zum Mitdenken, Weiterdenken, aber auch Nachdenken.
MOLUTAVA – FREIRAUM FÜR IDEEN
Ein Referenzbuch, d..
Aufgabenstellung
1. Kurzzusammenfassung der Ausschreibung
Die 4. Ausgabe des jährlichen Referenzbuchs der Industrie, FACTORY.onward MOLUTAVA 2025, erscheint im Oktober 2024. Für das Cover sucht der verlag-wendemark Verlag neue Vorschläge, die die Themen Freiraum und Wandel in den Fokus stellen.
2. Gestalterische & Inhaltliche Anforderungen
• Format: 195x250 mm + Anschnitt
• Rücken: ca. 1,6 cm (Stand letzte Publikation 2023)
• Auflösung: Druckqualität, mind. 300 dpi
• Inhaltliche Elemente:
- MOLUTAVA Schriftzug
- {polynesisch: Freiraum}
- Untersatz: Das Referenzbuch der Industrie. Für Vorwärtsdenker und Zukunftsmacher.
- part of FACTORY.onward Logo-Balken am unteren Rand (siehe Beispiel AuD_Titelbeispiel_Logobalken)
WICHTIG: Der aktuelle Schriftzug MOLUTAVA und die Farbe Orange (0/80/100/0) (siehe Beispiel MOLUTAVA 2021) sollen als Wiedererkennung in die Gestaltungen eingebunden werden.

```html
<!DOCTYPE html>
<html lang="de">
<head>
<meta charset="utf-8">
<title>MOLUTAVA 2024 – Cover</title>
<link href="https://fonts.googleapis.com/css2?family=Bebas+Neue&family=Oswald:wght@300;500;600&family=Roboto+Condensed:wght@500&display=swap" rel="stylesheet">
<style>
  :root {
    --orange: #e84e0f;
    --orange-deep: #c4420d;
    --white: #ffffff;
    --stage: #3a3a3a;
    --sky-top: #56627e;
    --sky-mid: #7d879d;
    --sky-low: #c9ced8;
  }
  html, body {
    margin: 0;
    width: 1200px;
    height: 1200px;
    overflow: hidden;
    background: var(--stage);
  }
  .cover {
    position: absolute;
    left: 151px;
    top: 25px;
    width: 897px;
    height: 1150px;
    overflow: hidden;
  }
  .cover-visual {
    position: absolute;
    inset: 0;
    background:
      radial-gradient(ellipse 55% 45% at 40% 40%, rgba(240,240,244,0.55), transparent 70%),
      linear-gradient(200deg, var(--sky-top) 0%, var(--sky-mid) 45%, var(--sky-low) 100%);
  }
  .title-stack {
    position: absolute;
    inset: 0;
  }
  .title-stack text {
    font-family: "Bebas Neue", "Oswald", sans-serif;
    font-size: 380px;
    fill: var(--orange);
  }
  .translation {
    position: absolute;
    left: 73px;
    top: 562px;
    margin: 0;
    font-family: "Roboto Condensed", sans-serif;
    font-weight: 500;
    font-size: 14px;
    color: var(--white);
  }
  .edition-year {
    position: absolute;
    right: 60px;
    top: 300px;
    margin: 0;
    font-family: "Oswald", sans-serif;
    font-weight: 600;
    font-size: 90px;
    line-height: 1;
    color: var(--orange);
  }
  .subtitle {
    position: absolute;
    right: 60px;
    top: 420px;
    margin: 0;
    text-align: right;
    font-family: "Oswald", sans-serif;
    font-weight: 300;
    font-size: 31px;
    line-height: 45px;
    color: var(--white);
  }
  .brand-band {
    position: absolute;
    left: 319px;
    right: 0;
    top: 1017px;
    height: 133px;
    background: linear-gradient(90deg, rgba(196,66,13,0.35) 0%, var(--orange-deep) 25%, var(--orange-deep) 100%);
  }
  .brand-line {
    position: absolute;
    right: 60px;
    top: 1062px;
    margin: 0;
    display: flex;
    align-items: baseline;
    gap: 16px;
    color: var(--white);
    font-family: "Oswald", sans-serif;
  }
  .brand-line .part-of {
    font-weight: 300;
    font-size: 26px;
  }
  .brand-line .brand-name {
    font-weight: 500;
    font-size: 46px;
    line-height: 1;
  }
</style>
</head>
<body>
  <main class="cover">
    <div class="cover-visual" role="img" aria-label="Weißer humanoider Roboter im Profil mit offenem, orange leuchtendem Schädel, die Hand nachdenklich am Kinn, vor grau-blauem Hintergrund"></div>

    <svg class="title-stack" viewBox="0 0 897 1150" aria-label="MOLUTAVA">
      <text x="0" y="265" textLength="306" lengthAdjust="spacingAndGlyphs">MO</text>
      <text x="0" y="546" textLength="306" lengthAdjust="spacingAndGlyphs">LU</text>
      <text x="0" y="866" textLength="306" lengthAdjust="spacingAndGlyphs">TA</text>
      <text x="0" y="1149" textLength="306" lengthAdjust="spacingAndGlyphs">VA</text>
    </svg>

    <p class="translation">{polynesisch – Freiraum}</p>

    <h2 class="edition-year">2024</h2>
    <p class="subtitle">Das Referenzbuch<br>der Industrie.<br>Für Vorwärtsdenker<br>und Zukunftsmacher.</p>

    <div class="brand-band"></div>
    <p class="brand-line"><span class="part-of">part of</span><span class="brand-name">FACTORY.onward</span></p>
  </main>
</body>
</html>
```